Experienced Home remodel service

I'm a home remodeler. I want a catch phrase that clearly describes viewers what kind of work I'm in like the purple phrase on my rough draft idea. I need my website, phone, logo, slogan included. The picture is of my daughter. I want her on it. Be cool if something could be added to her picture like a hard hat or tool belt ect and her picture cut out/background removed. Some kind of background other than plain white for whole picture. I added extra pics of her so pick one

Target Market(s)

Home owners between 30-60

Industry/Entity Type

Home renovation/remodel

Colors

Designer to choose colors to be used in the design.

Requirements
Must have
• Daughters picture incorporated. Logo, phone, website address, slogan,
Nice to have
• See a hardhat or tool belt added to one of my daughters pictures that is chosen to use by designer

```html
<!DOCTYPE html>
<html lang="en">
<head>
<meta charset="utf-8">
<title>Harlan Home Solutions – Billboard</title>
<link href="https://fonts.googleapis.com/css2?family=Montserrat:wght@500;600;700;800&display=swap" rel="stylesheet">
<style>
  :root {
    --page-bg: #8f8f8f;
    --ink: #111111;
    --navy: #123a93;
    --white: #ffffff;
    --sky-top: #dfeaf6;
    --sky-mid: #c9d8e8;
    --city: #8e99a5;
    --band-dark: rgba(70, 78, 90, 0.55);
    --band-light: rgba(255, 255, 255, 0.9);
  }
  * { box-sizing: border-box; margin: 0; padding: 0; }
  html, body { width: 992px; height: 1200px; overflow: hidden; }
  body {
    background: var(--page-bg);
    font-family: "Montserrat", Arial, sans-serif;
    position: relative;
  }
  .billboard {
    position: absolute;
    left: 16px;
    top: 360px;
    width: 960px;
    height: 480px;
    overflow: hidden;
  }
  .backdrop {
    position: absolute;
    inset: 0;
    background:
      linear-gradient(180deg, var(--sky-top) 0%, var(--sky-mid) 45%, var(--city) 100%);
  }
  .company-name {
    position: absolute;
    left: 41px;
    top: 30px;
    font-weight: 800;
    font-size: 58px;
    letter-spacing: -0.5px;
    color: var(--ink);
    white-space: nowrap;
  }
  .services {
    position: absolute;
    left: 217px;
    top: 112px;
    display: flex;
    gap: 30px;
    font-weight: 500;
    font-size: 26px;
    color: var(--ink);
    list-style: none;
  }
  .services li::before { content: "• "; }
  .brand-mark {
    position: absolute;
    left: 812px;
    top: 40px;
    width: 130px;
    display: flex;
    flex-direction: column;
    align-items: center;
    gap: 8px;
  }
  .brand-mark .mark-square {
    width: 54px;
    height: 54px;
    background: var(--ink);
  }
  .brand-mark .mark-name {
    font-weight: 800;
    font-size: 11px;
    line-height: 1.05;
    letter-spacing: 1px;
    color: var(--ink);
    text-align: center;
  }
  .slogan {
    position: absolute;
    left: 35px;
    top: 164px;
    width: 890px;
    height: 58px;
    background: var(--band-light);
    color: var(--navy);
    font-weight: 700;
    font-size: 45px;
    line-height: 58px;
    text-align: center;
    white-space: nowrap;
  }
  .phone-icon {
    position: absolute;
    left: 572px;
    top: 248px;
    width: 48px;
    height: 48px;
  }
  .phone-band {
    position: absolute;
    left: 190px;
    top: 307px;
    width: 770px;
    height: 96px;
    background: var(--band-light);
  }
  .phone-number {
    position: absolute;
    left: 286px;
    top: 304px;
    font-weight: 700;
    font-size: 88px;
    line-height: 100px;
    color: var(--navy);
    letter-spacing: 1px;
    white-space: nowrap;
  }
  .url-band {
    position: absolute;
    left: 190px;
    top: 403px;
    width: 770px;
    height: 77px;
    background: var(--band-dark);
  }
  .website {
    position: absolute;
    left: 279px;
    top: 418px;
    font-weight: 600;
    font-size: 35px;
    color: var(--white);
    white-space: nowrap;
  }
  .portrait {
    position: absolute;
    left: 54px;
    top: 252px;
    width: 206px;
    height: 228px;
    border-radius: 90px 90px 20px 20px;
    background: linear-gradient(180deg, #e8c64a 0%, #c9a07a 35%, #e4c9e6 70%, #d9b8de 100%);
  }
</style>
</head>
<body>
  <section class="billboard">
    <div class="backdrop" role="img" aria-label="Soft, out-of-focus city skyline with construction cranes under a pale blue sky"></div>

    <h1 class="company-name">Harlan Home Solutions</h1>
    <ul class="services">
      <li>Build</li>
      <li>Repair</li>
      <li>Replace</li>
    </ul>

    <div class="brand-mark">
      <span class="mark-square"></span>
      <span class="mark-name">HARLAN HOME<br>SOLUTIONS</span>
    </div>

    <p class="slogan">For All Your Home Remodel Needs</p>

    <svg class="phone-icon" viewBox="0 0 48 48" aria-hidden="true">
      <circle cx="24" cy="24" r="24" fill="var(--navy)"/>
      <path d="M17 12c1.2-.8 2.6-.5 3.3.7l2.4 4.2c.6 1 .3 2.3-.6 3l-1.7 1.3c1.2 2.8 3.4 5 6.2 6.3l1.3-1.7c.7-.9 2-1.2 3-.6l4.2 2.4c1.2.7 1.5 2.1.7 3.3l-1.6 2.3c-.9 1.3-2.6 1.8-4.1 1.2C22.5 32 16 25.5 13.8 17.7c-.5-1.5 0-3.2 1.3-4.1z" fill="var(--white)"/>
    </svg>

    <div class="phone-band"></div>
    <p class="phone-number">555-014-2273</p>

    <div class="url-band"></div>
    <p class="website">www.harlanhomesolutions.com</p>

    <div class="portrait" role="img" aria-label="Cut-out photo of the owner's smiling young daughter wearing a yellow hard hat and lilac coat, holding a hammer"></div>
  </section>
</body>
</html>
```